Brochure Design Project for Building Designer

I need a modern and edgy brochure to introduce my new business TORV Design, Commercial and Residential Building Designers.

We specialise in Building Design, Project Management and Design Consultation.

I would like the brochure to be anywhere between 2-4 pages, depending of amount of suitable content available.
Colours to be black and white with splashes of
bright colours (mostly incorporated in photos).

Main Content of brochure to be broken up into 3 (maybe 4) sections to include:

About Us
Services
Projects

Logo Text (DESIGN etc) can be changed to white if suits better with black background.

Would be nice to include sketches to give it that architectural feel.

Samples and wording will be uploaded shortly
Updates

I HAVE PROVIDED A COMPLETE UPDATE OF PROJECT REQUIREMENTS INCLUDING ALL NEW UPLOADED FILES.

PLEASE REFER TO THE BROCHURE LAYOUT PDF UPLOADEDĀ FOR FULL INFORMATION ON PROJECT INCLUDING BROCHURE LAYOUT.

IF YOU HAVE ANY QUESTIONS OR REQUIRE ANY FURTHER INFORMATION, PLEASE LET ME KNOW

I HAVE ADDED FURTHER DEVELOPED PDF DOCUMENTS OF BROCHURE.

IF YOU HAVE TROUBLE OPENING THESE DOCS IN ADOBE ILLUSTRATOR THRU ADOBE BRIDGE PLEASE LET ME KNOW & I WILL UPLOAD AI FILES.

CAN YOU PLEASE FINE TUNE GRAPHICS AND WORK ON BACKGROUND

Target Market(s)

Builders, Property Developers, Architects, Consultants, Professionals

Industry/Entity Type

Business

Requirements
Must have
• Very Professional Look
Black and White
Simple and easy to read layout
Either A4 (if only 2 pages) or
A3 double sided with centre fold (if 4 pages)
Touch up of photos (if possible) to make them stand out of the page.
Samples of recent projects with photos
Should not have
• Any comics or similar

```html
<!DOCTYPE html>
<html lang="en">
<head>
<meta charset="utf-8">
<title>TORV Design – About Us &amp; Services</title>
<link rel="stylesheet" href="https://fonts.googleapis.com/css2?family=Black+Ops+One&family=Inter:wght@300;400&display=swap">
<style>
  :root {
    --backdrop: #555555;
    --page: #ffffff;
    --ink: #1c1c1c;
    --ink-soft: #777777;
    --photo-light: #d9cfc3;
    --photo-mid: #a8978a;
    --photo-dark: #3a2f29;
    --quote-band: rgba(40, 40, 40, 0.78);
    --quote-text: #f2f2f2;
    --portrait: #6b5a4a;
  }
  * { margin: 0; padding: 0; box-sizing: border-box; }
  html, body { width: 1200px; height: 900px; overflow: hidden; }
  body {
    position: relative;
    background: var(--backdrop);
    font-family: "Inter", Arial, sans-serif;
    color: var(--ink);
  }
  .page {
    position: absolute;
    left: 34px; top: 51px;
    width: 1132px; height: 801px;
    background: var(--page);
  }
  .hero-photo {
    position: absolute;
    left: 0; top: 33px;
    width: 486px; height: 740px;
    background: linear-gradient(160deg, var(--photo-light) 0%, var(--photo-mid) 45%, var(--photo-dark) 100%);
  }
  .quote-band {
    position: absolute;
    left: 36px; top: 675px;
    width: 353px; height: 56px;
    background: var(--quote-band);
    color: var(--quote-text);
  }
  .quote-portrait {
    position: absolute;
    left: 6px; top: 4px;
    width: 52px; height: 48px;
    background: var(--portrait);
  }
  .quote-text {
    position: absolute;
    left: 64px; top: 5px;
    font-size: 17.5px; font-weight: 300;
    line-height: 17px; letter-spacing: 0.3px;
    text-transform: uppercase;
  }
  .quote-author {
    position: absolute;
    left: 66px; top: 41px;
    font-size: 10px; letter-spacing: 1.2px;
    text-transform: uppercase;
  }
  .section-title {
    position: absolute;
    left: 532px;
    font-family: "Black Ops One", Impact, sans-serif;
    font-size: 37px; letter-spacing: 3px;
    font-weight: 400; line-height: 1;
    color: var(--ink);
  }
  .section-title.about { top: 32px; }
  .section-title.services { top: 436px; }
  .title-slash { position: absolute; overflow: visible; }
  .lead, .closing {
    position: absolute;
    left: 535px;
    font-size: 15px; font-weight: 300;
    line-height: 21px;
    text-transform: uppercase;
    color: var(--ink);
  }
  .intro { position: absolute; left: 535px; font-size: 15px; font-weight: 300; }
  .bullet-list {
    position: absolute;
    left: 535px;
    list-style: none;
    font-size: 14.5px; font-weight: 300;
    line-height: 19px;
    color: var(--ink-soft);
  }
  .bullet-list li { display: flex; align-items: center; }
  .bullet-list li::before {
    content: "";
    width: 6px; height: 6px;
    margin-right: 6px;
    border: 1px solid var(--ink);
    border-radius: 50%;
    background: radial-gradient(circle, var(--ink) 0 1.2px, transparent 1.5px);
  }
</style>
</head>
<body>
  <main class="page">
    <div class="hero-photo" role="img" aria-label="Sepia photograph of a double-height living and dining room with a floating steel staircase, dark dining table and chairs"></div>
    <div class="quote-band">
      <div class="quote-portrait" role="img" aria-label="Small portrait of the quoted author"></div>
      <p class="quote-text">“Simplicity is th ultimate<br>sophistication”</p>
      <p class="quote-author">Aldo Verrani</p>
    </div>

    <h2 class="section-title about">About Us</h2>
    <svg class="title-slash" style="left:760px;top:28px" width="16" height="42"><line x1="1" y1="41" x2="14" y2="1" stroke="#555" stroke-width="1.2"/></svg>
    <p class="lead" style="top:78px">TORV Design has a diverse portfolio of commercial +<br>residential work across a range of scales, budgets +<br>project types. Areas of experience include:</p>
    <ul class="bullet-list" style="top:156px">
      <li>Commercial Developments</li>
      <li>Mixed-Use Developments</li>
      <li>Residential &amp; Multi Residential</li>
      <li>Upmarket Individual Houses</li>
      <li>Healthcare</li>
      <li>Commercial Industrial</li>
      <li>Cafes/Restaurants</li>
      <li>Alterations + Additions</li>
      <li>Residential + Commercial Interior Fitouts</li>
    </ul>
    <p class="lead" style="top:372px">We strive to be efficient at all times in every aspect of<br>our service + pride ourselves on our attention to detail.</p>

    <h2 class="section-title services">Services</h2>
    <svg class="title-slash" style="left:760px;top:432px" width="16" height="42"><line x1="1" y1="41" x2="14" y2="1" stroke="#555" stroke-width="1.2"/></svg>
    <p class="intro" style="top:477px">We are able to Provide a Wide Range of Services:</p>
    <ul class="bullet-list" style="top:501px">
      <li>Project Planning</li>
      <li>Design Concepts</li>
      <li>Design Development / Development Approval</li>
      <li>Consultant Liaison + Management</li>
      <li>Building Certification</li>
      <li>Tender / Construction Documentation</li>
      <li>Project Management</li>
      <li>3D Modelling &amp; Renders</li>
      <li>Re-Documentation &amp; Design Consultation</li>
      <li>Drafting Services</li>
    </ul>
    <p class="closing" style="top:709px">We offer high quality drafting solutions for pre-designed<br>projects of any size to ensure you get the best quality<br>drawings for local authority + construction issue.</p>
  </main>
</body>
</html>
```